BUSINESS CARD DESIGN

NAME- TODD MASVERIK
PHONE NUMER - 808- 451-7082
EMAIL- OFFICE@VORLINDE-GRADEWAY.COM
BACK OF CARD- SPEACIALIZES IN LAND CLEARING, FORESTRY MUCLHING AND EXCAVATION

Contact Information for Business Card

NAME- TODD MASVERIK PHONE NUMER - 808- 451-7082 EMAIL- OFFICE@VORLINDE-GRADEWAY.COM BACK OF CARD- SPEACIALIZES IN LAND CLEARING , MUCLHING AND EXCAVATION

```html
<!DOCTYPE html>
<html lang="en">
<head>
<meta charset="utf-8">
<title>Vorlinde Gradeway LLC – Business Card</title>
<link rel="stylesheet" href="https://fonts.googleapis.com/css2?family=Orbitron:wght@800;900&family=Roboto:wght@400;500&display=swap">
<style>
  :root {
    --backdrop: #1b1c1e;
    --card: #262628;
    --card-deep: #1f1f21;
    --gold: #fcb813;
    --edge: #f39a12;
    --ink: #111111;
    --white: #f4f4f4;
    --rule: #d9d9d9;
    --display: "Orbitron", "Arial Black", sans-serif;
    --body: "Roboto", Arial, sans-serif;
  }
  * { box-sizing: border-box; margin: 0; padding: 0; }
  html, body { width: 1200px; height: 840px; overflow: hidden; }
  body { background: var(--backdrop); position: relative; font-family: var(--body); }

  .card {
    position: absolute;
    width: 540px;
    height: 310px;
    border-radius: 22px;
    background: var(--card);
    border-bottom: 4px solid var(--edge);
    border-left: 2px solid var(--gold);
    overflow: hidden;
  }
  .card--back { left: 40px; top: 110px; }
  .card--front { left: 620px; top: 420px; }

  /* back side */
  .pattern-field {
    position: absolute; inset: 0;
    background: radial-gradient(ellipse at 80% 30%, #3a3a3c 0%, var(--card) 55%, var(--card-deep) 100%);
  }
  .back-content {
    position: absolute; inset: 0;
    display: flex; flex-direction: column; align-items: center; justify-content: center;
    gap: 14px;
  }
  .brand {
    display: flex; align-items: center; gap: 10px;
  }
  .brand-dot {
    width: 34px; height: 34px; border-radius: 50%; background: var(--gold);
  }
  .brand-name {
    font-family: var(--display); font-weight: 800; color: var(--gold);
    font-size: 20px; letter-spacing: 1px; line-height: 1.15;
  }
  .brand-name small { display: block; font-size: 11px; letter-spacing: 6px; }
  .specialty-tag {
    background: var(--gold); color: var(--ink);
    font-family: var(--display); font-weight: 800; font-size: 13px;
    padding: 3px 10px; letter-spacing: 0.5px;
  }
  .services {
    color: var(--white); font-size: 12px; letter-spacing: 0.4px;
  }
  .services .bullet { color: var(--gold); margin: 0 5px; }

  /* front side */
  .front-brand { position: absolute; left: 34px; top: 34px; }
  .front-brand .brand-dot { width: 56px; height: 56px; }
  .front-brand .brand-name { font-size: 22px; }
  .brand-phone {
    position: absolute; left: 34px; top: 104px;
    font-family: var(--display); font-weight: 800; color: var(--gold);
    font-size: 10px; letter-spacing: 7px;
  }
  .top-rule {
    position: absolute; left: 260px; right: 30px; top: 134px;
    height: 1px; background: var(--rule);
  }
  .person-name {
    position: absolute; left: 34px; top: 160px;
    font-family: var(--display); font-weight: 900; color: var(--gold);
    font-size: 28px; letter-spacing: 0.5px;
  }
  .name-rule {
    position: absolute; left: 34px; right: 30px; top: 208px;
    height: 1px; background: var(--rule);
  }
  .contact-row {
    position: absolute; left: 34px; right: 30px; top: 224px;
    display: flex; align-items: center; gap: 22px;
    color: var(--white); font-size: 17px;
  }
  .contact-item { display: flex; align-items: center; gap: 7px; }
  .contact-item svg { width: 16px; height: 16px; fill: var(--gold); flex: none; }
</style>
</head>
<body>

  <section class="card card--back" aria-label="Card back">
    <div class="pattern-field" role="img" aria-label="Subtle tonal background texture"></div>
    <div class="back-content">
      <div class="brand">
        <span class="brand-dot"></span>
        <p class="brand-name">VORLINDE GRADEWAY<small>LLC</small></p>
      </div>
      <p class="specialty-tag">SPEACIALIZES IN</p>
      <p class="services"><span class="bullet">●</span>LAND CLEARING<span class="bullet">●</span>MUCLHING<span class="bullet">●</span>EXCAVATION</p>
    </div>
  </section>

  <section class="card card--front" aria-label="Card front">
    <div class="brand front-brand">
      <span class="brand-dot"></span>
      <p class="brand-name">VORLINDE GRADEWAY<small>LLC</small></p>
    </div>
    <p class="brand-phone">808-451-7082</p>
    <span class="top-rule"></span>
    <h1 class="person-name">TODD MASVERIK</h1>
    <span class="name-rule"></span>
    <div class="contact-row">
      <p class="contact-item">
        <svg viewBox="0 0 24 24" aria-hidden="true"><path d="M6.6 10.8a15.1 15.1 0 0 0 6.6 6.6l2.2-2.2a1 1 0 0 1 1-.25 11.4 11.4 0 0 0 3.6.57 1 1 0 0 1 1 1V20a1 1 0 0 1-1 1A17 17 0 0 1 3 4a1 1 0 0 1 1-1h3.5a1 1 0 0 1 1 1c0 1.25.2 2.45.57 3.6a1 1 0 0 1-.25 1z"/></svg>
        808- 451-7082
      </p>
      <p class="contact-item">
        <svg viewBox="0 0 24 24" aria-hidden="true"><path d="M2 5h20v14H2zm2 2v.5l8 5 8-5V7zm0 2.8V17h16V9.8l-8 5z"/></svg>
        office@vorlinde-gradeway.com
      </p>
    </div>
  </section>

</body>
</html>
```